Commercial facility maintenance

I need a card design that helps my salesmen make contact with new clients, our product is facility maintenance and heavy industrial maintenance

```html
<!DOCTYPE html>
<html lang="en">
<head>
<meta charset="utf-8">
<title>Brandvale Millworks LLC – Business Card</title>
<link href="https://fonts.googleapis.com/css2?family=Montserrat:wght@400;500;700&display=swap" rel="stylesheet">
<style>
  :root {
    --page: #ffffff;
    --card: #1e1f23;
    --red: #b3293a;
    --white: #ffffff;
  }
  * { margin: 0; padding: 0; box-sizing: border-box; }
  html, body {
    width: 1200px; height: 1200px; overflow: hidden;
    background: var(--page);
    font-family: "Montserrat", sans-serif;
    color: var(--white);
  }
  .card {
    position: absolute; left: 221px; width: 765px; height: 438px;
    background: var(--card);
  }
  .card--front { top: 78px; }
  .card--back { top: 604px; }

  /* Front */
  .brand { position: absolute; left: 74px; top: 88px; display: flex; align-items: center; gap: 26px; }
  .brand__mark { width: 158px; height: 158px; border-radius: 50%; background: var(--red); flex: none; }
  .brand__name { font-weight: 700; color: var(--white); line-height: 1.05; letter-spacing: 1px; }
  .brand__name .line1 { display: block; font-size: 58px; }
  .brand__name .line2 { display: block; font-size: 32px; letter-spacing: 3px; }
  .rule-h { position: absolute; display: block; }
  .front-rule { left: 74px; top: 284px; width: 617px; height: 6px; }
  .tagline {
    position: absolute; left: 0; right: 0; top: 318px; text-align: center;
    font-size: 23px; font-weight: 400; letter-spacing: 4.2px;
  }

  /* Back */
  .person { position: absolute; left: 52px; top: 66px; }
  .person__name { font-size: 50px; font-weight: 700; letter-spacing: 1px; line-height: 1; }
  .person__title { font-size: 22px; font-weight: 500; margin-top: 8px; letter-spacing: .3px; }
  .back-rule { left: 0; top: 214px; width: 765px; height: 6px; }
  .divider { position: absolute; left: 378px; top: 234px; width: 6px; height: 204px; }

  .contacts { position: absolute; left: 44px; top: 264px; list-style: none; }
  .contacts li { display: flex; align-items: center; gap: 8px; height: 24px; font-size: 24px; font-weight: 400; }
  .contacts li + li { margin-top: 23px; }
  .contacts li:last-child { margin-top: 33px; }
  .contacts svg { width: 34px; height: 34px; flex: none; }

  .services { position: absolute; left: 404px; top: 261px; }
  .services__title { font-size: 24px; font-weight: 700; }
  .services ul { list-style: none; margin-top: 12px; }
  .services li { position: relative; padding-left: 28px; font-size: 24px; line-height: 35px; white-space: nowrap; }
  .services li::before {
    content: ""; position: absolute; left: 0; top: 11px;
    width: 15px; height: 15px; border-radius: 50%; background: var(--red);
  }
</style>
</head>
<body>

<section class="card card--front">
  <div class="brand">
    <span class="brand__mark"></span>
    <div class="brand__name">
      <span class="line1">BRANDVALE</span>
      <span class="line2">MILLWORKS LLC</span>
    </div>
  </div>
  <svg class="rule-h front-rule" viewBox="0 0 617 6" preserveAspectRatio="none"><polygon points="0,3 308,0 617,3 308,6" fill="var(--red)"/></svg>
  <p class="tagline">Reliable Industrial &amp; Facility Maintenance</p>
</section>

<section class="card card--back">
  <div class="person">
    <h1 class="person__name">JOHN SMITH</h1>
    <p class="person__title">Senior Maintennce Manager</p>
  </div>
  <svg class="rule-h back-rule" viewBox="0 0 765 6" preserveAspectRatio="none"><polygon points="0,3 382,0 765,3 382,6" fill="var(--red)"/></svg>
  <svg class="divider" viewBox="0 0 6 204" preserveAspectRatio="none"><polygon points="3,0 6,102 3,204 0,102" fill="var(--red)"/></svg>

  <ul class="contacts">
    <li>
      <svg viewBox="0 0 24 24"><path fill="var(--red)" d="M6.6 2.5c.6-.3 1.3 0 1.6.6l2 3.4c.3.6.1 1.3-.4 1.6L8.4 9c.9 2.4 2.6 4.4 4.8 5.7l1.3-1.2c.5-.4 1.2-.4 1.7 0l3 2.3c.5.4.6 1.1.3 1.6l-1.1 1.8c-.5.9-1.6 1.3-2.6 1C9.3 18.4 4.8 12.6 3.9 6.3c-.1-1 .4-2 1.3-2.6z"/></svg>
      (000) 000-000
    </li>
    <li>
      <svg viewBox="0 0 24 24"><rect x="1" y="5" width="22" height="15" fill="var(--red)"/><polyline points="1,5 12,13 23,5" fill="none" stroke="var(--card)" stroke-width="1.6"/></svg>
      john@brandvale.com
    </li>
    <li>
      <svg viewBox="0 0 24 24" fill="none" stroke="var(--red)" stroke-width="1"><circle cx="12" cy="12" r="10.5"/><ellipse cx="12" cy="12" rx="4.5" ry="10.5"/><line x1="12" y1="1.5" x2="12" y2="22.5"/><line x1="1.5" y1="12" x2="22.5" y2="12"/><line x1="3" y1="7" x2="21" y2="7"/><line x1="3" y1="17" x2="21" y2="17"/></svg>
      johnbrandvale.com
    </li>
  </ul>

  <div class="services">
    <h2 class="services__title">Specializing in:</h2>
    <ul>
      <li>Facility Maintenance</li>
      <li>Heavy Industrial Services</li>
    </ul>
  </div>
</section>

</body>
</html>
```